Fundraising Study Day East of England. Lift the January blues!

A flyer to advertise a fundraising event of lectures for dental hygienists and therapists in support of the exemption campaign. Currently dental hygienists and therapists require a prescription to deliver certain treatment or recommend certain toothpastes. If we are successful in the campaign we will be able to treat patients without these restrictions.

Industry/Entity Type

Dental

```html
<!DOCTYPE html>
<html lang="en">
<head>
<meta charset="utf-8">
<title>Fundraising Study Day East of England</title>
<link rel="stylesheet" href="https://fonts.googleapis.com/css2?family=Roboto:wght@400;700;900&family=Roboto+Condensed:wght@700&family=Arimo:wght@400;700&display=swap">
<style>
  :root{
    --navy:#0f4a86;
    --deep:#0b3b6e;
    --sky:#4faee2;
    --sky-light:#8fd0f1;
    --pale:#c4e7f8;
    --white:#ffffff;
    --ink:#1a2b3c;
    --text-blue:#2a78c0;
    --head-blue:#0d3f75;
  }
  *{box-sizing:border-box;margin:0;padding:0}
  html,body{width:681px;height:1200px;overflow:hidden;background:var(--white)}
  .flyer{position:relative;width:681px;height:1200px;overflow:hidden;
    background:linear-gradient(180deg,var(--sky) 0 150px,var(--sky-light) 150px 500px,var(--white) 500px);
    font-family:"Arimo",Arial,sans-serif;color:var(--ink)}
  .title-band{position:absolute;left:0;top:0;width:681px;height:150px;background:var(--navy)}
  .title{position:absolute;left:18px;top:14px;width:470px;font-family:"Roboto",Arial,sans-serif;
    font-weight:900;font-size:36px;line-height:1.08;color:var(--white);text-transform:uppercase;text-align:center;letter-spacing:.3px}
  .cost{position:absolute;left:490px;top:112px;width:175px;height:138px;background:var(--sky);
    border-radius:10px;box-shadow:0 4px 10px rgba(0,0,0,.25);text-align:center;color:var(--white);
    font-family:"Roboto Condensed",Arial,sans-serif;font-weight:700;z-index:2}
  .cost .label{display:block;font-size:38px;margin-top:8px}
  .cost .price{display:block;font-size:54px;line-height:1;margin-top:4px}
  .info{position:absolute;top:165px;left:0;width:480px;height:140px;background:var(--sky)}
  .info-col{position:absolute;top:12px;color:var(--white);font-size:15px;line-height:1.3}
  .info-col h2{font-family:"Roboto",Arial,sans-serif;font-weight:700;font-size:23px;margin-bottom:8px;letter-spacing:.5px}
  .info-col.location{left:40px}
  .info-col.datetime{left:205px}
  .photo{position:absolute;left:395px;top:255px;width:286px;height:460px}
  .photo-fill{position:absolute;inset:0;background:linear-gradient(160deg,#e6f3fb,#c9d9e3 45%,#a9c3d6);
    clip-path:path("M286 12 C200 -8 110 20 60 70 C20 115 20 200 35 280 C48 350 70 410 150 440 C200 455 250 450 286 440 Z")}
  .photo-frame{position:absolute;left:0;top:0}
  .intro{position:absolute;left:40px;top:330px;width:340px;font-size:15px;line-height:1.45;color:var(--ink);text-align:justify}
  .agenda-head{position:absolute;left:0;top:510px;width:300px;height:52px;background:var(--navy);
    border-radius:0 26px 26px 0}
  .agenda-head .tooth-icon{position:absolute;left:20px;top:6px}
  .agenda-head h2{position:absolute;left:78px;top:8px;font-family:"Roboto",Arial,sans-serif;
    font-weight:900;font-size:32px;color:var(--white);letter-spacing:1px}
  .registration{position:absolute;left:120px;top:575px;font-weight:700;font-size:16px;color:var(--head-blue)}
  .agenda{position:absolute;font-size:10.5px;line-height:1.3;color:var(--text-blue)}
  .agenda.left{left:40px;top:605px;width:270px}
  .agenda.right{left:330px;top:728px;width:260px}
  .slot{margin-bottom:12px}
  .slot .time{display:block;color:var(--head-blue);font-size:10.5px;margin-bottom:3px}
  .slot .speaker{display:block;font-weight:700;font-size:15px;color:var(--head-blue);margin-bottom:4px}
  .booking{font-size:11px;color:var(--text-blue);line-height:1.4}
  .booking strong{color:var(--head-blue)}
  .cartoon{position:absolute;left:0;top:955px;width:295px;height:245px;
    background:linear-gradient(180deg,#eaf5fc,#bfe0f4)}
  .footer-band{position:absolute;left:295px;top:1050px;width:386px;height:150px;background:var(--navy)}
  .footer-band h3{position:absolute;left:22px;top:14px;font-size:17px;font-weight:700;color:var(--white)}
  .footer-band .url{position:absolute;left:22px;top:46px;width:345px;font-size:13px;line-height:1.4;color:var(--white);word-break:break-all}
  .footer-band .sponsor{position:absolute;left:22px;top:128px;font-size:9px;color:var(--pale)}
</style>
</head>
<body>
<main class="flyer">
  <header class="title-band">
    <h1 class="title">Fundraising Study Day East of England. Lift the January Blues!</h1>
  </header>

  <section class="info">
    <div class="info-col location">
      <h2>LOCATION</h2>
      <p>Harlow Court Hotel<br>Linden Way<br>Stanbury<br>ST4 2QX</p>
    </div>
    <div class="info-col datetime">
      <h2>DATE AND TIME</h2>
      <p>Fri 19 January 2018<br>09:00 – 16:30 GMT</p>
    </div>
  </section>

  <div class="cost">
    <span class="label">Cost</span>
    <span class="price">£101.48</span>
  </div>

  <div class="photo">
    <div class="photo-fill" role="img" aria-label="Photograph of a smiling young couple holding a toothbrush, framed inside a tooth outline"></div>
    <svg class="photo-frame" width="286" height="460" viewBox="0 0 286 460" aria-hidden="true">
      <path d="M286 12 C200 -8 110 20 60 70 C20 115 20 200 35 280 C48 350 70 410 150 440 C200 455 250 450 286 440"
            fill="none" stroke="#ffffff" stroke-width="12"/>
    </svg>
  </div>

  <p class="intro">A fundraising event to support our exemptions project. The day will consist of a series of presentations ranging from the new ECPD to new technologies. The aim, being to enhance our learning and raise funds to support the exemptions campaign. The speakers line up includes some of the UK and Irelands most respected dental professionals in our field.</p>

  <div class="agenda-head">
    <svg class="tooth-icon" width="42" height="40" viewBox="0 0 42 40" aria-hidden="true">
      <path d="M8 4 C14 0 18 6 21 6 C24 6 28 0 34 4 C40 9 38 18 35 24 C33 30 32 38 28 38 C24 38 24 26 21 26 C18 26 18 38 14 38 C10 38 9 30 7 24 C4 18 2 9 8 4Z" fill="#ffffff"/>
    </svg>
    <h2>AGENDA</h2>
  </div>

  <p class="registration">09:00 - 09:30 Registration</p>

  <section class="agenda left">
    <div class="slot">
      <span class="time">9:30 - 10:15</span>
      <span class="speaker">Clare Wendell:</span>
      Immediate past president of the NADT will be updating us on all things ECPD.
    </div>
    <div class="slot">
      <span class="time">10:15 - 11:00</span>
      <span class="speaker">RosaLinley:</span>
      Will provide an update on teeth whitening and explain how social media has impacted her business.
    </div>
    <div class="slot">
      <span class="time">11:00 - 11:30 Break</span>
      <span class="time">11:30 - 13:00</span>
      <span class="speaker">Nadia Crowe &amp; HelenMarsh:</span>
      Will be providing a combined presentation on 'Scaling your business' and 'start to finish' practice techniques. The aim being to build our business with effective communication systems and protocols. This session promotes audience participation!
    </div>
  </section>

  <section class="agenda right">
    <div class="slot"><span class="time">13:00 - 14:00 Lunch</span></div>
    <div class="slot">
      <span class="time">14:00 - 15:00</span>
      <span class="speaker">Priya Sethi:</span>
      Save your back. All things posture
    </div>
    <div class="slot"><span class="time">15:00 - 15:30 Break</span></div>
    <div class="slot">
      <span class="time">15:30 - 16:30</span>
      <span class="speaker">Laura Pennick:</span>
      Our internationally acclaimed speaker will update our knowledge of periodontal disease and nutrition and new technologies
    </div>
    <p class="booking">To book, please email<br><strong>Helen Marsh</strong> - helen@helenmarsh-events.co.uk</p>
  </section>

  <div class="cartoon" role="img" aria-label="Cartoon of a row of teeth with a speech bubble joking about personal space"></div>

  <footer class="footer-band">
    <h3>Please visit URL below for more info:</h3>
    <p class="url">https://www.eventsignup.co.uk/e/fundraising-study-day-east-of-england-lift-the-january-blues-tickets-48120337</p>
    <p class="sponsor">Flyer sponsored by Brightline Dental</p>
  </footer>
</main>
</body>
</html>
```